Double sided business card design for Orbit 2019 - Logo already done

Double sided business card that uses the EPS vector logo we''ve already had designed (files attached).

Target Market(s)

15, 18, 21 and over 30

Industry/Entity Type

Business

Requirements
Must have
• The same color writting as the design on the logo
Nice to have
• Company name: Orbit Entertainment 2019
• Full Name:         Mr T.Welmoth
•                          Brackley Row
•                          Hertfordshire
•                          KT19 3PL
•                          England

• Choices between the different versions.
Should not have
• Anything offensive.

```html
<!DOCTYPE html>
<html lang="en">
<head>
<meta charset="utf-8">
<title>Orbit Entertainment 2019 – Business Card</title>
<link href="https://fonts.googleapis.com/css2?family=Cabin:wght@400&display=swap" rel="stylesheet">
<style>
  :root {
    --teal: #007a99;
    --paper: #ffffff;
  }
  html, body {
    margin: 0;
    padding: 0;
    overflow: hidden;
    background: var(--paper);
  }
  .card {
    position: relative;
    width: 1200px;
    height: 727px;
    background: var(--paper);
    overflow: hidden;
    font-family: "Cabin", "Gill Sans", sans-serif;
    font-weight: 400;
    color: var(--teal);
  }
  .holder-name {
    position: absolute;
    left: 445px;
    top: 303px;
    margin: 0;
    font-size: 27px;
    letter-spacing: -0.3px;
  }
  .name-rule {
    position: absolute;
    left: 369px;
    top: 342px;
    width: 455px;
    height: 2px;
    background: var(--teal);
  }
  .company-name {
    position: absolute;
    left: 842px;
    top: 325px;
    margin: 0;
    font-size: 27px;
    letter-spacing: -0.3px;
    white-space: nowrap;
  }
  .address {
    position: absolute;
    left: 445px;
    top: 487px;
    margin: 0;
    font-style: normal;
    font-size: 24px;
    line-height: 26px;
    letter-spacing: -0.3px;
  }
  .footer-band {
    position: absolute;
    left: 369px;
    top: 609px;
    width: 831px;
    height: 83px;
    background: var(--teal);
  }
</style>
</head>
<body>
  <div class="card">
    <p class="holder-name">Mr T.Welmoth</p>
    <div class="name-rule"></div>

    <p class="company-name">Orbit Entertainment 2019</p>

    <address class="address">
      Brackley Row<br>
      Hertfordshire<br>
      KT19 3PL England
    </address>

    <div class="footer-band"></div>
  </div>
</body>
</html>
```